TriVex Business Card Design - double sided -plumbing local plumbing company

We have a Plumbing company where the design was create through Sketch Hive. We would now like a business card designed as well. We want it to be in the colour version of the logo.

Details below for the card.

Phone Number: 0438 615 247
Email: info@trivexplumbing.example.au
Website: https://trivexplumbing.example.au
We really want a sophisticated design that stand out from the other- informative and timeless.

Target Market(s)

local Canberra market

Industry/Entity Type

Plumbing, gas fitting, hot water

Contact Information for Business Card

Phone number, email, logo and "Supplying all your heating, cooling and hot water needs"

Requirements
Must have
• bust be colourful, must also be though about it being printed on a magnet. must Vex with the logo - I dont want the logo and information chucked onto a white canvas I would prefer it to be smooth and look purposeful

```html
<!DOCTYPE html>
<html lang="en">
<head>
<meta charset="utf-8">
<title>TriVex Plumbing – Business Card</title>
<link rel="stylesheet" href="https://fonts.googleapis.com/css2?family=Montserrat:ital,wght@0,400;0,500;0,700;1,400&display=swap">
<style>
  :root {
    --backdrop: #0587cc;
    --card-white: #ffffff;
    --brand-blue: #00a6e6;
    --brand-orange: #f6a534;
    --navy: #001c36;
    --navy-glow: #0b2642;
    --ink-grey: #5c5c5c;
    --divider: #d9d4c8;
    --icon-tan: #b9ae98;
  }
  * { margin: 0; padding: 0; box-sizing: border-box; }
  html, body {
    width: 1200px; height: 1145px; overflow: hidden;
    background: var(--backdrop);
    font-family: "Montserrat", sans-serif;
  }
  .sheet {
    position: relative; width: 1200px; height: 1145px;
  }
  .card {
    position: absolute; left: 164px;
    width: 872px; height: 496px;
    overflow: hidden;
    box-shadow: 0 8px 24px rgba(0, 30, 60, 0.25);
  }
  .card-front { top: 52px; background: var(--card-white); }
  .card-back { top: 596px; background: var(--navy); }

  /* front */
  .front-wave { position: absolute; left: 0; top: 0; width: 872px; height: 496px; }
  .brand-name {
    position: absolute; left: 90px; top: 232px;
    font-weight: 700; font-size: 50px; line-height: 1;
    color: var(--brand-blue); letter-spacing: 1px;
  }
  .divider {
    position: absolute; left: 465px; top: 174px;
    width: 2px; height: 172px; background: var(--divider);
  }
  .person { position: absolute; left: 523px; top: 176px; }
  .person-name {
    font-weight: 700; font-size: 38px; line-height: 1.05;
    color: var(--brand-blue);
  }
  .person-title {
    font-style: italic; font-size: 18px; color: var(--ink-grey);
    margin-top: 2px;
  }
  .contact-list { list-style: none; margin-top: 14px; }
  .contact-list li {
    display: flex; align-items: center;
    font-size: 16px; color: var(--ink-grey);
    height: 29.5px;
  }
  .contact-list svg { width: 16px; height: 16px; margin-right: 14px; flex: none; }
  .tagline {
    position: absolute; left: 340px; top: 410px; width: 380px;
    text-align: center; font-size: 15px; line-height: 19px; color: var(--ink-grey);
  }

  /* back */
  .back-glow { position: absolute; left: 0; top: 0; width: 872px; height: 496px; }
  .back-brand {
    position: absolute; left: 0; right: 0; top: 210px;
    text-align: center; color: var(--card-white);
    font-weight: 700; font-size: 66px; line-height: 1; letter-spacing: 2px;
  }
</style>
</head>
<body>
<main class="sheet">

  <section class="card card-front" aria-label="Business card front">
    <svg class="front-wave" viewBox="0 0 872 496" aria-hidden="true">
      <path d="M0 380 C160 392 330 468 530 488 C700 504 820 420 872 360 L872 496 L0 496 Z" fill="var(--brand-orange)"/>
      <path d="M0 390 C160 402 330 478 530 497 L872 497 L872 374 C820 432 700 512 530 497 Z" fill="var(--brand-blue)"/>
      <path d="M0 390 C160 402 330 478 530 497 C700 512 820 432 872 374 L872 496 L0 496 Z" fill="var(--brand-blue)"/>
    </svg>

    <div class="brand-name">TriVex</div>
    <div class="divider"></div>

    <div class="person">
      <h1 class="person-name">Liam Hart</h1>
      <p class="person-title">Chief Operating Officer</p>
      <ul class="contact-list">
        <li>
          <svg viewBox="0 0 16 16" aria-hidden="true"><path d="M3.5 1.5 L6 4 L4.6 5.8 C5.5 7.8 8.2 10.5 10.2 11.4 L12 10 L14.5 12.5 L12.8 14.3 C8 14 2 8 1.7 3.2 Z" fill="var(--icon-tan)"/></svg>
          0438 615 247
        </li>
        <li>
          <svg viewBox="0 0 16 16" aria-hidden="true"><circle cx="8" cy="8" r="6.4" fill="none" stroke="var(--icon-tan)" stroke-width="1.3"/><circle cx="8" cy="8" r="2.5" fill="none" stroke="var(--icon-tan)" stroke-width="1.3"/><path d="M10.5 5.5 V9.5 C10.5 11 12.5 11 13 9.5" fill="none" stroke="var(--icon-tan)" stroke-width="1.3"/></svg>
          info@trivexplumbing.example.au
        </li>
        <li>
          <svg viewBox="0 0 16 16" aria-hidden="true"><circle cx="8" cy="8" r="6.8" fill="var(--icon-tan)"/><path d="M1.5 8 H14.5 M8 1.2 V14.8 M8 1.2 C4.5 4.5 4.5 11.5 8 14.8 M8 1.2 C11.5 4.5 11.5 11.5 8 14.8 M2.5 4.8 H13.5 M2.5 11.2 H13.5" fill="none" stroke="#fff" stroke-width="0.8"/></svg>
          www.trivexplumbing.example.au
        </li>
      </ul>
    </div>

    <p class="tagline">Supplying all your heating,<br>cooling and hot water needs</p>
  </section>

  <section class="card card-back" aria-label="Business card back">
    <svg class="back-glow" viewBox="0 0 872 496" aria-hidden="true">
      <circle cx="436" cy="250" r="238" fill="var(--navy-glow)"/>
    </svg>
    <div class="back-brand">TriVex Plumbing</div>
  </section>

</main>
</body>
</html>
```